Create Print and Packaging Designs for nivalo rice

dear all , we are required our rice packaging design on the urgent basis maximum by sunday night tomorrow with ready features in the related software ( Photo shop or coral draw) . the free lancer have to provide us the source files with all related things by which printing company can print the bag and make the cylinders. We require very elegant and good looking design . The project will be awarded only to those who will cooperate with us properly by phone and Skype and meet or required quality standards . This clearly means that only those will win the project who will cooperate with us in the terms until printing of the rice bag . By the extra efforts we believe on to pay even extra reward but the work should be completed.

Our Branch name is NIVALO Rice.

we will write on front Original Basmati Rice . Use logo only if it suits . other wise no logo

the measurement of rice bag is attached .
Regarding the product we are offering the premium quality basmati rice. The colour matching preferable will be Royal Blue .

For quality of design i would like to mention here that we are competing with big brands like Silver Meadow Rice and Morvan Rice. reference is available on the website of related companies.

if you need further information please send me e mail .

nivalorice@postvane.com

```html
<!DOCTYPE html>
<html lang="en">
<head>
<meta charset="utf-8">
<title>NIVALO Rice – Original Basmati Rice 5kg</title>
<link rel="stylesheet" href="https://fonts.googleapis.com/css2?family=Cinzel:wght@700&family=Kaushan+Script&family=Noto+Naskh+Arabic:wght@500;700&family=Arimo:wght@400&display=swap">
<style>
  :root {
    --crimson: #c3161c;
    --crimson-deep: #8c0c11;
    --maroon: #5b1312;
    --maroon-dark: #3e0b0b;
    --stripe: rgba(70, 6, 8, 0.55);
    --gold: #b3874f;
    --gold-light: #e0b56d;
    --gold-box: #a98150;
    --cream: #fff6ea;
    --badge-text: #e9a184;
    --badge-fill: #a5161a;
  }
  html, body {
    margin: 0;
    padding: 0;
    overflow: hidden;
    background: #ffffff;
  }
  .rice-bag {
    position: relative;
    width: 928px;
    height: 1200px;
    overflow: hidden;
    font-family: "Arimo", Arial, sans-serif;
  }
  .damask-field {
    position: absolute;
    inset: 0;
    background:
      radial-gradient(ellipse at 50% 55%, #7a1a17 0%, var(--maroon) 55%, var(--maroon-dark) 100%);
  }
  .bag-shapes {
    position: absolute;
    inset: 0;
  }
  .tagline {
    position: absolute;
    top: 218px;
    left: 0;
    width: 100%;
    text-align: center;
    font-family: "Kaushan Script", cursive;
    font-size: 23px;
    color: var(--cream);
    letter-spacing: 0.5px;
  }
  .brand-name {
    position: absolute;
    top: 252px;
    left: 0;
    width: 100%;
    text-align: center;
    font-family: "Cinzel", serif;
    font-weight: 700;
    font-size: 118px;
    line-height: 1;
    color: var(--gold);
    letter-spacing: 4px;
  }
  .product-name {
    position: absolute;
    top: 384px;
    left: 0;
    width: 100%;
    text-align: center;
    font-size: 36px;
    color: #ffffff;
    letter-spacing: 0.5px;
  }
  .product-name-ar {
    position: absolute;
    top: 450px;
    left: 273px;
    width: 375px;
    height: 57px;
    background: var(--gold-box);
    color: var(--cream);
    font-family: "Noto Naskh Arabic", serif;
    font-weight: 500;
    font-size: 32px;
    line-height: 57px;
    text-align: center;
  }
  .net-weight {
    position: absolute;
    top: 1005px;
    left: 390px;
    width: 148px;
    text-align: center;
    font-family: "Cinzel", serif;
    font-weight: 700;
    color: var(--gold);
  }
  .net-weight .amount {
    font-size: 50px;
  }
  .net-weight .unit {
    font-size: 30px;
  }
  .net-weight-ar {
    position: absolute;
    top: 1085px;
    left: 390px;
    width: 148px;
    text-align: center;
    font-family: "Noto Naskh Arabic", serif;
    font-weight: 700;
    font-size: 44px;
    color: var(--gold);
  }
  .feature-badge {
    position: absolute;
    top: 1054px;
    width: 131px;
    height: 62px;
    box-sizing: border-box;
    border-radius: 6px;
    background: var(--badge-fill);
    border: 1px solid rgba(233, 161, 132, 0.35);
    color: var(--badge-text);
    font-size: 17px;
    line-height: 21px;
    display: flex;
    align-items: center;
    justify-content: center;
    text-align: center;
  }
  .badge-aromatic { left: 91px; }
  .badge-taste { left: 241px; }
  .badge-quality { left: 557px; }
  .badge-aged { left: 706px; }
</style>
</head>
<body>
  <main class="rice-bag">
    <div class="damask-field" role="img" aria-label="Ornate gold damask scroll pattern on deep red"></div>

    <svg class="bag-shapes" width="928" height="1200" viewBox="0 0 928 1200" aria-hidden="true">
      <defs>
        <linearGradient id="crown-band" x1="0" y1="0" x2="0" y2="1">
          <stop offset="0" stop-color="#a80f15"/>
          <stop offset="0.6" stop-color="var(--crimson)"/>
          <stop offset="1" stop-color="#d01a20"/>
        </linearGradient>
        <linearGradient id="gold-edge" x1="0" y1="0" x2="1" y2="0">
          <stop offset="0" stop-color="#9c7444"/>
          <stop offset="0.5" stop-color="var(--gold-light)"/>
          <stop offset="1" stop-color="#9c7444"/>
        </linearGradient>
      </defs>

      <rect class="centre-stripe" x="273" y="430" width="377" height="770" fill="var(--stripe)"/>

      <path class="crown-band" d="M0 0 H928 V433 Q464 667 0 433 Z" fill="url(#crown-band)"/>
      <path class="crown-edge" d="M0 433 Q464 667 928 433" fill="none" stroke="url(#gold-edge)" stroke-width="4"/>
      <path class="crown-rim" d="M0 448 Q464 690 928 448 V433 Q464 667 0 433 Z" fill="var(--crimson-deep)"/>

      <path class="weight-ribbon" d="M390 922 L464 948 L538 922 V1200 H390 Z" fill="var(--badge-fill)"/>
      <rect class="weight-rule" x="380" y="1070" width="168" height="4" fill="var(--gold)"/>
    </svg>

    <p class="tagline" style="margin:0">Enjoy The Real Taste, Aroma &amp; Freshness</p>
    <h1 class="brand-name" style="margin:0">NIVALO</h1>
    <h2 class="product-name" style="margin:0;font-weight:400">ORIGINAL BASMATI RICE</h2>
    <div class="product-name-ar" lang="ar" dir="rtl">أرزَ بسمَتي أصيل</div>

    <div class="net-weight"><span class="amount">5</span><span class="unit">kg</span></div>
    <div class="net-weight-ar" lang="ar" dir="rtl">٥ كغ</div>

    <div class="feature-badge badge-aromatic">Highly<br>Aromatic</div>
    <div class="feature-badge badge-taste">Supreme<br>Taste</div>
    <div class="feature-badge badge-quality">Premium<br>Quality</div>
    <div class="feature-badge badge-aged">Long<br>Aged</div>
  </main>
</body>
</html>
```